Welding company needs a business card

We are looking for a logo and business card.

Contact Information for Business Card

418 Cobblestone Lane
York, PA 17402
410-555-0173
Rmfabworksco@quorvamail.com

```html
<!DOCTYPE html>
<html lang="en">
<head>
<meta charset="utf-8">
<title>RM Fabworks Co — Business Card</title>
<link rel="stylesheet" href="https://fonts.googleapis.com/css2?family=Lato:wght@300;400;700;900&display=swap">
<style>
  :root {
    --backdrop: #2a2a2a;
    --card: #0d0d0d;
    --card-edge: #1a1a1a;
    --ink: #f2f2f2;
    --ink-soft: #c9c9c9;
    --rule: #8a8a8a;
  }
  * { margin: 0; padding: 0; box-sizing: border-box; }
  html, body {
    width: 1200px; height: 900px; overflow: hidden;
    background: var(--backdrop);
    font-family: "Lato", Arial, sans-serif;
  }
  .stage {
    width: 1200px; height: 900px;
    display: flex; flex-direction: column;
    align-items: center; justify-content: center; gap: 40px;
  }
  .card {
    width: 630px; height: 360px;
    background: var(--card);
    border: 1px solid var(--card-edge);
    position: relative;
    color: var(--ink);
  }
  .card-front {
    display: flex; align-items: center; justify-content: center;
  }
  .brand-name {
    font-weight: 900; font-size: 54px; letter-spacing: 2px;
    color: var(--ink-soft); text-transform: uppercase;
  }
  .card-back .identity {
    position: absolute; right: 345px; top: 128px;
    text-align: right;
  }
  .person-name {
    font-size: 22px; font-weight: 400; letter-spacing: 1px;
    text-transform: uppercase;
  }
  .person-role {
    font-size: 17px; font-weight: 300; color: var(--ink-soft); margin-top: 2px;
  }
  .divider {
    position: absolute; left: 316px; top: 122px;
    width: 1px; height: 62px; background: var(--rule);
  }
  .contact-list {
    position: absolute; left: 340px; top: 138px;
    list-style: none; font-size: 18px; font-weight: 400;
  }
  .contact-list li { display: flex; align-items: center; gap: 8px; line-height: 24px; }
  .contact-list svg { width: 16px; height: 16px; fill: var(--ink); }
  .address {
    position: absolute; left: 0; right: 0; top: 252px;
    text-align: center; font-size: 18px; font-weight: 400;
  }
</style>
</head>
<body>
<main class="stage">
  <section class="card card-front">
    <h1 class="brand-name">RM Fabworks Co</h1>
  </section>

  <section class="card card-back">
    <div class="identity">
      <p class="person-name">Daniel Brooks</p>
      <p class="person-role">Managing Director</p>
    </div>
    <span class="divider"></span>
    <ul class="contact-list">
      <li>
        <svg viewBox="0 0 24 24" aria-hidden="true"><path d="M3 6c0-1 1-2 2-2h14c1 0 2 1 2 2v3h-5V7H8v2H3zM6 11h12l3 8H3zm6 2a2.5 2.5 0 1 0 0 5 2.5 2.5 0 0 0 0-5z"/></svg>
        410-555-0173
      </li>
      <li>
        <svg viewBox="0 0 24 24" aria-hidden="true"><path d="M2 5h20v14H2zm2 2v.5l8 5.5 8-5.5V7l-8 5.5z"/></svg>
        Rmfabworksco@quorvamail.com
      </li>
    </ul>
    <p class="address">418 Cobblestone Lane York, PA 17402</p>
  </section>
</main>
</body>
</html>
```